Menu Design for coffee shop/cafe

We need a menu designed for our cafe/coffee shop. We want to go for a pretty floral/rustic look, white washed, dusty pinks and beige. Our logo has a birdcage, and the cafe decor will have birdcages, flowers to match this. We would like for everything to fit onto an A3 or A2 double sided. including drinks, and we are looking at a separate smaller option for kids menu, which can include a colouring in section on the one side.

```html
<!DOCTYPE html>
<html lang="en">
<head>
<meta charset="utf-8">
<title>The Linden Cafe — Menu</title>
<link href="https://fonts.googleapis.com/css2?family=Alfa+Slab+One&family=Caveat:wght@500;700&family=Roboto+Slab:wght@700&display=swap" rel="stylesheet">
<style>
  :root {
    --canvas: #ffffff;
    --chalk: #2c3a3b;
    --chalk-deep: #1f2a2b;
    --header: #7a4a38;
    --panel: rgba(224, 172, 156, 0.9);
    --panel-light: rgba(236, 180, 165, 0.88);
    --row-line: rgba(255, 255, 255, 0.75);
    --text-light: #ffffff;
    --brand: #d8a77c;
    --kid-orange: #f49a69;
    --kid-yellow: #eec653;
    --kid-green: #95c1a2;
    --kid-purple: #caa3cb;
  }
  * { box-sizing: border-box; margin: 0; padding: 0; }
  html, body { width: 1200px; height: 2200px; overflow: hidden; background: var(--canvas); }
  .canvas { position: relative; width: 1200px; height: 2200px; }

  .page {
    position: absolute; left: 309px; width: 530px; height: 750px; overflow: hidden;
    box-shadow: 6px 8px 14px rgba(0,0,0,0.28);
  }
  .page--front { top: 265px; background: linear-gradient(160deg, var(--chalk) 0%, var(--chalk-deep) 100%); }
  .page--back { top: 1175px; background: #ffffff; }

  .art { position: absolute; }
  .art--coffee-cup { left: 316px; top: 6px; width: 214px; height: 222px;
    background: radial-gradient(circle at 62% 38%, #e9d6bf 0 22%, #7a4a2c 34%, #3b2216 60%, rgba(44,58,59,0) 78%); }
  .art--flowers { left: 0; top: 640px; width: 530px; height: 110px;
    background: linear-gradient(180deg, rgba(44,58,59,0) 0%, #6b2e2e 45%, #3a2220 100%); }
  .art--branch-birds { left: 250px; top: 0; width: 280px; height: 270px;
    background: radial-gradient(ellipse at 75% 35%, #d8d6d6 0%, #eeeded 55%, rgba(255,255,255,0) 80%); }
  .art--juice { left: 230px; top: 400px; width: 90px; height: 210px;
    background: linear-gradient(180deg, #ffd35a, #f3a21a); }
  .art--fruit { left: 0; top: 590px; width: 530px; height: 160px;
    background: linear-gradient(90deg, #f3d046 0%, #e6473a 35%, #f39a2a 65%, #9bc25a 100%); }

  .brand { position: absolute; left: 15px; width: 232px; top: 70px; display: flex; align-items: center; justify-content: center; gap: 10px; }
  .brand__dot { width: 14px; height: 14px; border-radius: 50%; background: var(--brand); }
  .brand__name { font-family: "Caveat", cursive; font-weight: 700; font-size: 40px; color: var(--brand); line-height: 1; }

  .menu { position: absolute; display: flex; flex-direction: column; }
  .menu__title {
    height: 42px; background: var(--header); color: var(--text-light);
    font-family: "Alfa Slab One", serif; font-size: 21px; letter-spacing: 1.5px;
    display: flex; align-items: center; justify-content: center;
  }
  .menu__list { flex: 1; background: var(--panel); list-style: none; display: flex; flex-direction: column; justify-content: space-evenly; padding: 6px 10px; }
  .menu__item { display: flex; align-items: center; gap: 8px; color: var(--text-light); }
  .menu__name { font-family: "Caveat", cursive; font-weight: 500; font-size: 13px; white-space: nowrap; width: 58px; }
  .menu__rule { flex: 1; height: 1px; background: var(--row-line); }
  .menu__price { font-family: "Roboto Slab", serif; font-weight: 700; font-size: 13px; width: 30px; text-align: right; }

  .menu--coffee { left: 15px; top: 193px; width: 232px; height: 451px; }
  .menu--drinks { left: 276px; top: 276px; width: 232px; height: 449px; }
  .menu--other { left: 15px; top: 188px; width: 226px; height: 438px; }
  .menu--other .menu__list { background: var(--panel-light); }

  .menu--kids { left: 270px; top: 267px; width: 226px; height: 419px; }
  .menu--kids .menu__title { height: 45px; }
  .menu--kids .menu__list { padding: 0; gap: 1px; background: #ffffff; justify-content: stretch; }
  .menu--kids .menu__item { flex: 1; padding: 0 10px; }
  .menu__item--orange { background: var(--kid-orange); }
  .menu__item--yellow { background: var(--kid-yellow); }
  .menu__item--green { background: var(--kid-green); }
  .menu__item--purple { background: var(--kid-purple); }
</style>
</head>
<body>
<main class="canvas">

  <section class="page page--front">
    <div class="art art--coffee-cup" role="img" aria-label="Photo of a cup of coffee on a saucer surrounded by roasted coffee beans"></div>
    <div class="art art--flowers" role="img" aria-label="Photo of dark red and pink roses along the bottom edge"></div>

    <div class="brand"><span class="brand__dot"></span><span class="brand__name">The Linden Cafe</span></div>

    <div class="menu menu--coffee">
      <h2 class="menu__title">COFFEE</h2>
      <ul class="menu__list">
        <li class="menu__item"><span class="menu__name">Lorem Ipsum</span><span class="menu__rule"></span><span class="menu__price">10$</span></li>
        <li class="menu__item"><span class="menu__name">Lorem Ipsum</span><span class="menu__rule"></span><span class="menu__price">10$</span></li>
        <li class="menu__item"><span class="menu__name">Lorem Ipsum</span><span class="menu__rule"></span><span class="menu__price">10$</span></li>
        <li class="menu__item"><span class="menu__name">Lorem Ipsum</span><span class="menu__rule"></span><span class="menu__price">10$</span></li>
        <li class="menu__item"><span class="menu__name">Lorem Ipsum</span><span class="menu__rule"></span><span class="menu__price">10$</span></li>
        <li class="menu__item"><span class="menu__name">Lorem Ipsum</span><span class="menu__rule"></span><span class="menu__price">10$</span></li>
        <li class="menu__item"><span class="menu__name">Lorem Ipsum</span><span class="menu__rule"></span><span class="menu__price">10$</span></li>
        <li class="menu__item"><span class="menu__name">Lorem Ipsum</span><span class="menu__rule"></span><span class="menu__price">10$</span></li>
        <li class="menu__item"><span class="menu__name">Lorem Ipsum</span><span class="menu__rule"></span><span class="menu__price">10$</span></li>
        <li class="menu__item"><span class="menu__name">Lorem Ipsum</span><span class="menu__rule"></span><span class="menu__price">10$</span></li>
        <li class="menu__item"><span class="menu__name">Lorem Ipsum</span><span class="menu__rule"></span><span class="menu__price">10$</span></li>
        <li class="menu__item"><span class="menu__name">Lorem Ipsum</span><span class="menu__rule"></span><span class="menu__price">10$</span></li>
        <li class="menu__item"><span class="menu__name">Lorem Ipsum</span><span class="menu__rule"></span><span class="menu__price">10$</span></li>
        <li class="menu__item"><span class="menu__name">Lorem Ipsum</span><span class="menu__rule"></span><span class="menu__price">10$</span></li>
        <li class="menu__item"><span class="menu__name">Lorem Ipsum</span><span class="menu__rule"></span><span class="menu__price">10$</span></li>
        <li class="menu__item"><span class="menu__name">Lorem Ipsum</span><span class="menu__rule"></span><span class="menu__price">10$</span></li>
        <li class="menu__item"><span class="menu__name">Lorem Ipsum</span><span class="menu__rule"></span><span class="menu__price">10$</span></li>
        <li class="menu__item"><span class="menu__name">Lorem Ipsum</span><span class="menu__rule"></span><span class="menu__price">10$</span></li>
      </ul>
    </div>

    <div class="menu menu--drinks">
      <h2 class="menu__title">DRINKS</h2>
      <ul class="menu__list">
        <li class="menu__item"><span class="menu__name">Lorem Ipsum</span><span class="menu__rule"></span><span class="menu__price">10$</span></li>
        <li class="menu__item"><span class="menu__name">Lorem Ipsum</span><span class="menu__rule"></span><span class="menu__price">10$</span></li>
        <li class="menu__item"><span class="menu__name">Lorem Ipsum</span><span class="menu__rule"></span><span class="menu__price">10$</span></li>
        <li class="menu__item"><span class="menu__name">Lorem Ipsum</span><span class="menu__rule"></span><span class="menu__price">10$</span></li>
        <li class="menu__item"><span class="menu__name">Lorem Ipsum</span><span class="menu__rule"></span><span class="menu__price">10$</span></li>
        <li class="menu__item"><span class="menu__name">Lorem Ipsum</span><span class="menu__rule"></span><span class="menu__price">10$</span></li>
        <li class="menu__item"><span class="menu__name">Lorem Ipsum</span><span class="menu__rule"></span><span class="menu__price">10$</span></li>
        <li class="menu__item"><span class="menu__name">Lorem Ipsum</span><span class="menu__rule"></span><span class="menu__price">10$</span></li>
        <li class="menu__item"><span class="menu__name">Lorem Ipsum</span><span class="menu__rule"></span><span class="menu__price">10$</span></li>
        <li class="menu__item"><span class="menu__name">Lorem Ipsum</span><span class="menu__rule"></span><span class="menu__price">10$</span></li>
        <li class="menu__item"><span class="menu__name">Lorem Ipsum</span><span class="menu__rule"></span><span class="menu__price">10$</span></li>
        <li class="menu__item"><span class="menu__name">Lorem Ipsum</span><span class="menu__rule"></span><span class="menu__price">10$</span></li>
        <li class="menu__item"><span class="menu__name">Lorem Ipsum</span><span class="menu__rule"></span><span class="menu__price">10$</span></li>
        <li class="menu__item"><span class="menu__name">Lorem Ipsum</span><span class="menu__rule"></span><span class="menu__price">10$</span></li>
        <li class="menu__item"><span class="menu__name">Lorem Ipsum</span><span class="menu__rule"></span><span class="menu__price">10$</span></li>
        <li class="menu__item"><span class="menu__name">Lorem Ipsum</span><span class="menu__rule"></span><span class="menu__price">10$</span></li>
        <li class="menu__item"><span class="menu__name">Lorem Ipsum</span><span class="menu__rule"></span><span class="menu__price">10$</span></li>
        <li class="menu__item"><span class="menu__name">Lorem Ipsum</span><span class="menu__rule"></span><span class="menu__price">10$</span></li>
      </ul>
    </div>
  </section>

  <section class="page page--back">
    <div class="art art--branch-birds" role="img" aria-label="Illustration of a tree branch with a hanging birdcage and flying birds"></div>
    <div class="art art--juice" role="img" aria-label="Photo of a glass of orange juice"></div>
    <div class="art art--fruit" role="img" aria-label="Photo of sliced lemon, grapefruit, orange and apple"></div>

    <div class="brand"><span class="brand__dot"></span><span class="brand__name">The Linden Cafe</span></div>

    <div class="menu menu--other">
      <h2 class="menu__title">OTHER MENU</h2>
      <ul class="menu__list">
        <li class="menu__item"><span class="menu__name">Lorem Ipsum</span><span class="menu__rule"></span><span class="menu__price">10$</span></li>
        <li class="menu__item"><span class="menu__name">Lorem Ipsum</span><span class="menu__rule"></span><span class="menu__price">10$</span></li>
        <li class="menu__item"><span class="menu__name">Lorem Ipsum</span><span class="menu__rule"></span><span class="menu__price">10$</span></li>
        <li class="menu__item"><span class="menu__name">Lorem Ipsum</span><span class="menu__rule"></span><span class="menu__price">10$</span></li>
        <li class="menu__item"><span class="menu__name">Lorem Ipsum</span><span class="menu__rule"></span><span class="menu__price">10$</span></li>
        <li class="menu__item"><span class="menu__name">Lorem Ipsum</span><span class="menu__rule"></span><span class="menu__price">10$</span></li>
        <li class="menu__item"><span class="menu__name">Lorem Ipsum</span><span class="menu__rule"></span><span class="menu__price">10$</span></li>
        <li class="menu__item"><span class="menu__name">Lorem Ipsum</span><span class="menu__rule"></span><span class="menu__price">10$</span></li>
        <li class="menu__item"><span class="menu__name">Lorem Ipsum</span><span class="menu__rule"></span><span class="menu__price">10$</span></li>
        <li class="menu__item"><span class="menu__name">Lorem Ipsum</span><span class="menu__rule"></span><span class="menu__price">10$</span></li>
        <li class="menu__item"><span class="menu__name">Lorem Ipsum</span><span class="menu__rule"></span><span class="menu__price">10$</span></li>
        <li class="menu__item"><span class="menu__name">Lorem Ipsum</span><span class="menu__rule"></span><span class="menu__price">10$</span></li>
        <li class="menu__item"><span class="menu__name">Lorem Ipsum</span><span class="menu__rule"></span><span class="menu__price">10$</span></li>
        <li class="menu__item"><span class="menu__name">Lorem Ipsum</span><span class="menu__rule"></span><span class="menu__price">10$</span></li>
        <li class="menu__item"><span class="menu__name">Lorem Ipsum</span><span class="menu__rule"></span><span class="menu__price">10$</span></li>
        <li class="menu__item"><span class="menu__name">Lorem Ipsum</span><span class="menu__rule"></span><span class="menu__price">10$</span></li>
        <li class="menu__item"><span class="menu__name">Lorem Ipsum</span><span class="menu__rule"></span><span class="menu__price">10$</span></li>
        <li class="menu__item"><span class="menu__name">Lorem Ipsum</span><span class="menu__rule"></span><span class="menu__price">10$</span></li>
      </ul>
    </div>

    <div class="menu menu--kids">
      <h2 class="menu__title">KIDS MENU</h2>
      <ul class="menu__list">
        <li class="menu__item menu__item--orange"><span class="menu__name">Lorem Ipsum</span><span class="menu__rule"></span><span class="menu__price">10$</span></li>
        <li class="menu__item menu__item--yellow"><span class="menu__name">Lorem Ipsum</span><span class="menu__rule"></span><span class="menu__price">10$</span></li>
        <li class="menu__item menu__item--green"><span class="menu__name">Lorem Ipsum</span><span class="menu__rule"></span><span class="menu__price">10$</span></li>
        <li class="menu__item menu__item--purple"><span class="menu__name">Lorem Ipsum</span><span class="menu__rule"></span><span class="menu__price">10$</span></li>
        <li class="menu__item menu__item--orange"><span class="menu__name">Lorem Ipsum</span><span class="menu__rule"></span><span class="menu__price">10$</span></li>
        <li class="menu__item menu__item--yellow"><span class="menu__name">Lorem Ipsum</span><span class="menu__rule"></span><span class="menu__price">10$</span></li>
        <li class="menu__item menu__item--green"><span class="menu__name">Lorem Ipsum</span><span class="menu__rule"></span><span class="menu__price">10$</span></li>
        <li class="menu__item menu__item--purple"><span class="menu__name">Lorem Ipsum</span><span class="menu__rule"></span><span class="menu__price">10$</span></li>
        <li class="menu__item menu__item--orange"><span class="menu__name">Lorem Ipsum</span><span class="menu__rule"></span><span class="menu__price">10$</span></li>
        <li class="menu__item menu__item--yellow"><span class="menu__name">Lorem Ipsum</span><span class="menu__rule"></span><span class="menu__price">10$</span></li>
        <li class="menu__item menu__item--green"><span class="menu__name">Lorem Ipsum</span><span class="menu__rule"></span><span class="menu__price">10$</span></li>
        <li class="menu__item menu__item--purple"><span class="menu__name">Lorem Ipsum</span><span class="menu__rule"></span><span class="menu__price">10$</span></li>
        <li class="menu__item menu__item--orange"><span class="menu__name">Lorem Ipsum</span><span class="menu__rule"></span><span class="menu__price">10$</span></li>
        <li class="menu__item menu__item--yellow"><span class="menu__name">Lorem Ipsum</span><span class="menu__rule"></span><span class="menu__price">10$</span></li>
      </ul>
    </div>
  </section>

</main>
</body>
</html>
```